IT business looking for Standout Letterhead Design

We need a letterhead design for a company based in San Diego, CA called Corvane Systems, Inc. We specialize in IT engineering, installation and technical support pertaining to the department of defense.

We would like to see a design that incorporates the black and gold that matches our company logo.

More information on the company can be found at www.corvane-sys.example

```html
<!DOCTYPE html>
<html lang="en">
<head>
<meta charset="utf-8">
<title>Corvane Systems, Inc. — Letterhead</title>
<link rel="stylesheet" href="https://fonts.googleapis.com/css2?family=Ubuntu:wght@700&family=Libre+Baskerville:wght@400;700&display=swap">
<style>
  :root {
    --ink: #111111;
    --band: #000000;
    --gold: #a89a1c;
    --gold-soft: #b5a72a;
    --paper: #ffffff;
    --frame: #8a8a8a;
    --rule: #222222;
    --mark: #ecebe7;
  }
  * { margin: 0; padding: 0; box-sizing: border-box; }
  html, body { width: 843px; height: 1200px; overflow: hidden; background: var(--paper); }
  .letterhead {
    position: relative;
    width: 843px;
    height: 1200px;
    background: var(--paper);
    border: 1px solid var(--frame);
    overflow: hidden;
    font-family: "Libre Baskerville", Georgia, serif;
    color: var(--ink);
  }
  .header-band, .footer-band { position: absolute; left: 0; width: 843px; display: block; }
  .header-band { top: 0; height: 60px; }
  .footer-band { bottom: 0; height: 46px; }

  .brand-name {
    position: absolute;
    left: 10px;
    top: 38px;
    font-family: "Libre Baskerville", Georgia, serif;
    font-size: 12px;
    line-height: 14px;
    font-weight: 400;
    color: var(--ink);
    letter-spacing: 0.5px;
  }
  .company-title {
    position: absolute;
    left: 0; right: 0;
    top: 4px;
    text-align: center;
    font-family: "Ubuntu", Arial, sans-serif;
    font-weight: 700;
    font-size: 24px;
    line-height: 30px;
    color: var(--gold);
  }
  .company-tagline {
    position: absolute;
    left: 0; right: 0;
    top: 40px;
    text-align: center;
    font-family: "Ubuntu", Arial, sans-serif;
    font-weight: 700;
    font-size: 12px;
    line-height: 14px;
    color: var(--gold);
  }

  .field {
    position: absolute;
    top: 108px;
    font-size: 14px;
    line-height: 18px;
    display: flex;
    align-items: baseline;
  }
  .field-date { left: 22px; }
  .field-ref { right: 22px; }
  .field-line {
    display: inline-block;
    width: 84px;
    border-bottom: 1px solid var(--rule);
    margin-left: 6px;
    transform: translateY(-3px);
  }
  .field-ref .field-line { margin-left: 2px; }

  .backdrop-mark {
    position: absolute;
    left: 270px;
    top: 430px;
    width: 300px;
    height: 340px;
    border-radius: 40px;
    background: radial-gradient(ellipse at center, var(--mark) 0%, rgba(236,235,231,0.5) 55%, rgba(255,255,255,0) 75%);
  }

  .footer-address {
    position: absolute;
    left: 0; right: 0;
    top: 1138px;
    text-align: center;
    font-size: 14px;
    line-height: 16px;
    font-weight: 700;
    color: var(--ink);
  }
  .footer-contact {
    position: absolute;
    left: 0; right: 0;
    text-align: center;
    font-size: 14px;
    line-height: 16px;
    font-weight: 700;
    color: var(--gold-soft);
  }
  .footer-phone { top: 1164px; }
  .footer-web { top: 1181px; }
</style>
</head>
<body>
  <main class="letterhead">
    <svg class="header-band" viewBox="0 0 843 60" preserveAspectRatio="none" aria-hidden="true">
      <defs>
        <linearGradient id="headerFade" x1="0" y1="0" x2="1" y2="0">
          <stop offset="0" stop-color="#ffffff"/>
          <stop offset="0.06" stop-color="#d8d8d8"/>
          <stop offset="0.17" stop-color="#000000"/>
          <stop offset="1" stop-color="#000000"/>
        </linearGradient>
      </defs>
      <path d="M0 0 H843 V36 Q 600 40 420 46 Q 260 50 140 44 Q 60 40 0 42 Z" fill="url(#headerFade)"/>
    </svg>

    <div class="brand-name">CORVANE</div>
    <div class="company-title">Corvane Systems Inc.</div>
    <div class="company-tagline">Deals in IT Engineering, Installation &amp; Technical Support</div>

    <div class="field field-date">Date:<span class="field-line"></span></div>
    <div class="field field-ref">Reference #:<span class="field-line"></span></div>

    <div class="backdrop-mark" role="img" aria-label="Faint shield emblem watermark area"></div>

    <div class="footer-address">Corvane Systems, Incorporation, San Diego, CA</div>

    <svg class="footer-band" viewBox="0 0 843 46" preserveAspectRatio="none" aria-hidden="true">
      <defs>
        <linearGradient id="footerFade" x1="0" y1="0" x2="1" y2="0">
          <stop offset="0" stop-color="#000000"/>
          <stop offset="0.76" stop-color="#000000"/>
          <stop offset="0.9" stop-color="#8a8a8a"/>
          <stop offset="1" stop-color="#ffffff"/>
        </linearGradient>
      </defs>
      <path d="M0 10 Q 200 6 420 7 Q 640 8 843 2 V46 H0 Z" fill="url(#footerFade)"/>
    </svg>

    <div class="footer-contact footer-phone">Phone: 555-010-4827, Facsimile: 555-010-4830</div>
    <div class="footer-contact footer-web">www.corvane-sys.example, e-mail: info@corvane-sys.example</div>
  </main>
</body>
</html>
```